Flyer-Design für regional agierendes Immobilienbüro
Zielgruppe
*regional agierendes Immobilienbüro
*Vermittlung von privaten Wohnimmobilien (Einfamilienhäuser, Wohnungen, Grundstücke)
*projektbezogene Zielgruppe: Immobilien Eigentümer / Verkäufer /Vermieter
*Idee: Gutschein über eine von drei Serviceleistungen - kostenlos*:
- Wertermittlung vom geprüften Preisbild-Berater
- Wohnflächen-Check
- Unterlagen-Check
*für Verkäufer / Vermieter im Wert von EUR 349,-
Aufgabenstellung
*CI (Style Guide, diverse Grafiken und Logos in verschiedenen Formaten vorhanden)
*cleanes, modernes Design - dennoch Eyecatcher (Postwurf)
*Ggf. DIN lang
Der Schlüssel zu einem erfolgreichen Verkauf liegt in der sorgfältigen Vorbereitung!
Passt der Verkaufspreis?
Sind alle Unterlagen vollständig und vorab auf mögliche 'Stolpersteine' geprüft?
Stimmt die Wohnfläche und sind alle Angaben rechtssicher korrekt?
Gerne prüfen wir, ob die grundlegenden Voraussetzungen für einen reibungslosen Verkauf Ihrer Immobilie zum bestmöglichen Verkaufspreis passen - kostenlos und unverbindlich! Im Rahmen eines unverbindlichen Beratungsgesprächs erfahren Sie auch, wie Sie von unserem vollumfänglichen Vermarktungsservice profitieren können.
Rufen Sie am besten gleich an und vereinbaren Sie einen Termin mit uns!

```html
<!DOCTYPE html>
<html lang="de">
<head>
<meta charset="utf-8">
<title>Lindhofer Immobilien – Flyer DIN lang</title>
<link rel="stylesheet" href="https://fonts.googleapis.com/css2?family=Raleway:wght@400&family=Roboto+Condensed:ital,wght@1,300&display=swap">
<style>
  :root {
    --page-bg: #ffffff;
    --petrol-dark: #02526a;
    --petrol-light: #33718f;
    --divider: #ffffff;
    --text-light: #ffffff;
    --wall-light: #e6e3dc;
    --wall-mid: #b9b7b2;
    --suit-navy: #1e2a45;
    --suit-deep: #141d33;
  }
  * { margin: 0; padding: 0; box-sizing: border-box; }
  html, body {
    width: 849px;
    height: 1200px;
    overflow: hidden;
    background: var(--page-bg);
  }
  .flyer {
    position: absolute;
    left: 222px;
    top: 176px;
    width: 404px;
    height: 849px;
    background: var(--divider);
    box-shadow: 2px 3px 5px rgba(0, 0, 0, 0.18);
  }
  .brand-band {
    position: absolute;
    left: 0; top: 0;
    width: 404px;
    height: 282px;
    background: linear-gradient(to bottom, var(--petrol-dark) 0%, var(--petrol-dark) 35%, var(--petrol-light) 100%);
    color: var(--text-light);
    text-align: center;
  }
  .brand-mark {
    position: absolute;
    left: 163px;
    top: 69px;
    width: 80px;
    height: 80px;
  }
  .brand-name {
    position: absolute;
    left: 0; right: 0;
    top: 175px;
    font-family: "Raleway", sans-serif;
    font-weight: 400;
    font-size: 18px;
    letter-spacing: 17px;
    padding-left: 17px;
    line-height: 1;
  }
  .brand-tagline {
    position: absolute;
    left: 0; right: 0;
    top: 207px;
    font-family: "Raleway", sans-serif;
    font-weight: 400;
    font-size: 8px;
    letter-spacing: 7.5px;
    padding-left: 7.5px;
    line-height: 1;
  }
  .portrait {
    position: absolute;
    left: 0; top: 285px;
    width: 404px;
    height: 419px;
    background:
      radial-gradient(ellipse 70% 45% at 40% 100%, var(--suit-deep) 0%, var(--suit-navy) 55%, transparent 100%),
      linear-gradient(to bottom, var(--wall-light) 0%, var(--wall-mid) 45%, var(--suit-navy) 78%, var(--suit-deep) 100%);
  }
  .quote-band {
    position: absolute;
    left: 0; top: 707px;
    width: 404px;
    height: 142px;
    background: linear-gradient(to bottom, var(--petrol-dark) 0%, var(--petrol-light) 100%);
    display: flex;
    align-items: center;
    justify-content: center;
  }
  .quote {
    font-family: "Roboto Condensed", sans-serif;
    font-style: italic;
    font-weight: 300;
    font-size: 18px;
    line-height: 29px;
    color: var(--text-light);
    text-align: center;
    letter-spacing: -0.6px;
    margin-top: -2px;
  }
</style>
</head>
<body>
  <main class="flyer">
    <header class="brand-band">
      <svg class="brand-mark" viewBox="0 0 80 80" aria-hidden="true">
        <circle cx="40" cy="40" r="38" fill="none" stroke="#ffffff" stroke-width="1.2"/>
      </svg>
      <div class="brand-name">LINDHOFER</div>
      <div class="brand-tagline">IMMOBILIEN</div>
    </header>
    <div class="portrait" role="img" aria-label="Porträtfoto des Maklers im dunkelblauen Anzug mit hellblauer Krawatte vor heller Wand"></div>
    <section class="quote-band">
      <p class="quote">“Der Schlüssel zu einem erfolgreichen<br>Verkauf Ihrer Immobilie liegt in der<br>sorgfältigen Vorbereitung!”</p>
    </section>
  </main>
</body>
</html>
```